Business Cards Letter Head Financial Trading Company
Bus Cards Letter Head Compliment Slips
Simple
Oliver Petchley
Managing Director
Level 52
8 Harrow Crescent
Fenmoor Quay
London
E17 3RT
oliver.petchley@zqtrading.co.uk
www.zoltavequitytrading.co.uk
Would like additional cards for other employees
Logo on back page

```html
<!DOCTYPE html>
<html lang="en">
<head>
<meta charset="utf-8">
<title>Zoltav Equity Trading – Business Cards</title>
<link rel="stylesheet" href="https://fonts.googleapis.com/css2?family=Marcellus&family=Marcellus+SC&display=swap">
<style>
  :root {
    --page: #eef0f3;
    --card: #ffffff;
    --purple: #3a2f8c;
    --purple-deep: #2a2170;
    --gold: #c9a25a;
    --gold-light: #e6c98e;
    --ink-light: #ffffff;
    --grey: #7a7a86;
  }
  * { box-sizing: border-box; margin: 0; padding: 0; }
  html, body { width: 1200px; height: 980px; overflow: hidden; }
  body {
    background: var(--page);
    position: relative;
    font-family: "Marcellus", serif;
  }
  .card {
    position: absolute;
    width: 700px;
    height: 400px;
    background: var(--card);
    border-radius: 26px;
    overflow: hidden;
    box-shadow: 0 10px 28px rgba(40, 40, 70, 0.18);
  }
  .card--back { left: 440px; top: 90px; }
  .card--front { left: 60px; top: 490px; }

  /* Back */
  .back-mark {
    position: absolute;
    left: 0; right: 0; top: 120px;
    display: flex; align-items: center; justify-content: center; gap: 18px;
  }
  .mark-dot {
    width: 54px; height: 54px; border-radius: 50%;
    background: var(--gold);
  }
  .brand-name {
    font-family: "Marcellus", serif;
    color: var(--purple);
    font-size: 34px;
    letter-spacing: 1px;
  }
  .back-web {
    position: absolute;
    left: 0; right: 0; top: 250px;
    text-align: center;
    font-family: "Marcellus SC", serif;
    color: var(--grey);
    font-size: 17px;
    letter-spacing: 5px;
  }

  /* Front */
  .front-wave { position: absolute; left: 0; top: 0; width: 700px; height: 400px; }
  .front-brand {
    position: absolute;
    left: 60px; top: 78px;
    display: flex; align-items: center; gap: 16px;
  }
  .front-brand .brand-name { font-size: 38px; }
  .front-brand .mark-dot { width: 46px; height: 46px; }
  .contact {
    position: absolute;
    top: 250px;
    color: var(--ink-light);
    font-family: "Marcellus SC", serif;
    font-size: 14px;
    line-height: 20px;
    letter-spacing: 0.6px;
  }
  .contact--person { left: 40px; width: 290px; text-align: right; }
  .contact--person .person-name { font-size: 16px; }
  .contact--lines { left: 370px; list-style: none; }
  .contact--lines li { display: flex; align-items: center; gap: 10px; height: 24px; }
  .contact--lines svg { width: 18px; height: 18px; flex: none; }
  .contact-divider {
    position: absolute; left: 350px; top: 252px;
    width: 1px; height: 94px; background: var(--gold-light);
  }
</style>
</head>
<body>

<section class="card card--back" aria-label="Business card back">
  <div class="back-mark">
    <span class="mark-dot"></span>
    <span class="brand-name">Zoltav Equity Trading</span>
  </div>
  <p class="back-web">www.zoltavequitytrading.co.uk</p>
</section>

<section class="card card--front" aria-label="Business card front">
  <svg class="front-wave" viewBox="0 0 700 400" preserveAspectRatio="none" aria-hidden="true">
    <defs>
      <linearGradient id="goldSweep" x1="0" x2="1" y1="0" y2="0">
        <stop offset="0" stop-color="#e6c98e"/>
        <stop offset="0.5" stop-color="#c9a25a"/>
        <stop offset="1" stop-color="#e6c98e"/>
      </linearGradient>
    </defs>
    <path d="M0 200 C 180 150, 330 250, 520 205 C 600 186, 660 180, 700 190 L700 222 C 650 208, 590 214, 520 232 C 330 280, 180 180, 0 228 Z" fill="url(#goldSweep)"/>
    <path d="M0 228 C 180 180, 330 280, 520 232 C 590 214, 650 208, 700 222 L700 400 L0 400 Z" fill="#3a2f8c"/>
  </svg>

  <div class="front-brand">
    <span class="mark-dot"></span>
    <span class="brand-name">Zoltav Equity Trading</span>
  </div>

  <div class="contact contact--person">
    <p class="person-name">Oliver Petchley</p>
    <p>Managing Director</p>
    <p>Level 52 | 8 Harrow Crescent</p>
    <p>Fenmoor Quay | London E17 3RT</p>
  </div>

  <span class="contact-divider"></span>

  <ul class="contact contact--lines">
    <li>
      <svg viewBox="0 0 20 20"><circle cx="10" cy="10" r="10" fill="#c9a25a"/><path d="M7 5h2l1 3-1.3 1a6 6 0 0 0 2.3 2.3L12 10l3 1v2c0 .6-.4 1-1 1A9 9 0 0 1 6 6c0-.6.4-1 1-1z" fill="#fff"/></svg>
      <span>020 7946 0183</span>
    </li>
    <li>
      <svg viewBox="0 0 20 20"><circle cx="10" cy="10" r="10" fill="#c9a25a"/><rect x="7" y="4" width="6" height="12" rx="1" fill="#fff"/><rect x="8" y="5.5" width="4" height="7.5" fill="#c9a25a"/></svg>
      <span>+44 7700 900412</span>
    </li>
    <li>
      <svg viewBox="0 0 20 20"><circle cx="10" cy="10" r="10" fill="#c9a25a"/><rect x="5" y="6.5" width="10" height="7" fill="#fff"/><path d="M5 6.5l5 4 5-4" fill="none" stroke="#c9a25a" stroke-width="1"/></svg>
      <span>oliver.petchley@zqtrading.co.uk</span>
    </li>
    <li>
      <svg viewBox="0 0 20 20"><circle cx="10" cy="10" r="10" fill="#c9a25a"/><circle cx="10" cy="10" r="5" fill="none" stroke="#fff" stroke-width="1.2"/><path d="M5 10h10M10 5c-2 3-2 7 0 10M10 5c2 3 2 7 0 10" fill="none" stroke="#fff" stroke-width="1"/></svg>
      <span>www.zoltavequitytrading.co.uk</span>
    </li>
  </ul>
</section>

</body>
</html>
```